Business Card and Stationery for Bellwick Home Services
Bellwick Home Services
Professional
R. Owen Tallis
President/CEO
4187 Marrow Creek Lane,
Suite K
Baton Rouge LA 70342
rowentallis@bellwickhomeservices.biz
www.bellwickhomeservice.biz
Commercial License # 53419 Residential LIcense # 21398
The color formula for the orange is:
C=0 M=74 Y=100 K=0
We take care of all of your home needs.
Plumbing, Heating and AIr, Electrical, Remodeling, Roofing, New Construction, Insurance Damage Repairs, Fire Restoration, if its in you home, we can service it or take care of it for you!!!
THESE ARE JUST IDEAS, want to use the back for information, etc.......maybe a light watermark on the back, using part of the logo, showing under the lettering. Would like the back to be the orange color

```html
<!DOCTYPE html>
<html lang="en">
<head>
<meta charset="utf-8">
<title>Bellwick Home Services – Business Card</title>
<link href="https://fonts.googleapis.com/css2?family=Open+Sans:wght@400;600;700&display=swap" rel="stylesheet">
<style>
  :root {
    --orange: #f15a22;
    --orange-deep: #d9480f;
    --slate-dark: #2c343c;
    --slate-mid: #47525c;
    --ink: #3a3a3a;
    --muted: #6d6d6d;
    --paper: #ffffff;
    --paper-shade: #e9e9e9;
    --backdrop: #d8d4cf;
    --brand-square: #8a4a24;
  }
  * { box-sizing: border-box; margin: 0; padding: 0; }
  html, body { width: 1200px; height: 896px; overflow: hidden; }
  body {
    background: var(--backdrop);
    font-family: "Open Sans", Arial, sans-serif;
    position: relative;
  }
  .card {
    position: absolute;
    width: 560px;
    height: 320px;
    background: var(--paper);
    box-shadow: 0 6px 18px rgba(0,0,0,.25);
    overflow: hidden;
  }
  .card--front { left: 70px; top: 70px; }
  .card--back {
    left: 570px; top: 490px;
    background: linear-gradient(180deg, #f7f7f7 0%, var(--paper-shade) 100%);
  }

  .front__header {
    height: 150px;
    background: repeating-linear-gradient(90deg, rgba(255,255,255,.03) 0 6px, rgba(0,0,0,.04) 6px 12px),
                linear-gradient(180deg, var(--slate-mid) 0%, var(--slate-dark) 100%);
    display: flex; align-items: center; justify-content: center;
    border-bottom: 4px solid #c9c9c9;
  }

  .brand { display: flex; align-items: center; gap: 14px; }
  .brand__mark {
    width: 78px; height: 78px; border-radius: 14px;
    background: var(--brand-square);
  }
  .brand__name {
    font-weight: 700; font-size: 26px; line-height: 1.1;
    color: var(--orange); width: 170px;
  }

  .front__body {
    display: flex; justify-content: space-between;
    padding: 22px 34px 0 36px;
  }
  .person__name { color: var(--orange); font-weight: 600; font-size: 15px; }
  .person__title { color: var(--ink); font-size: 12px; margin-top: 3px; }

  .contact { list-style: none; font-size: 9.5px; color: var(--muted); width: 205px; }
  .contact li { display: flex; align-items: flex-start; gap: 7px; line-height: 1.45; }
  .contact svg { flex: none; margin-top: 2px; }
  .contact__address { margin-bottom: 2px; }

  .back__brand { position: absolute; left: 0; right: 0; top: 108px; display: flex; justify-content: center; }
  .back__stripe { position: absolute; left: 0; bottom: 22px; }
</style>
</head>
<body>

<section class="card card--front">
  <header class="front__header">
    <div class="brand">
      <div class="brand__mark"></div>
      <div class="brand__name">Bellwick Home Services</div>
    </div>
  </header>
  <div class="front__body">
    <div class="person">
      <p class="person__name">R. Owen Tallis</p>
      <p class="person__title">President/CEO</p>
    </div>
    <ul class="contact">
      <li class="contact__address">
        <svg width="9" height="9" viewBox="0 0 10 10"><circle cx="5" cy="5" r="5" fill="var(--orange)"/></svg>
        <span>4187 Marrow Creek Lane,<br>Suite K<br>Baton Rouge LA 70342</span>
      </li>
      <li><svg width="9" height="9" viewBox="0 0 10 10"><circle cx="5" cy="5" r="5" fill="var(--orange)"/></svg><span>225-555-0148</span></li>
      <li><svg width="9" height="9" viewBox="0 0 10 10"><circle cx="5" cy="5" r="5" fill="var(--orange)"/></svg><span>225-555-0193</span></li>
      <li><svg width="9" height="9" viewBox="0 0 10 10"><circle cx="5" cy="5" r="5" fill="var(--orange)"/></svg><span>504-555-0127</span></li>
      <li><svg width="9" height="9" viewBox="0 0 10 10"><circle cx="5" cy="5" r="5" fill="var(--orange)"/></svg><span>rowentallis@bellwickhomeservices.biz</span></li>
      <li><svg width="9" height="9" viewBox="0 0 10 10"><circle cx="5" cy="5" r="5" fill="var(--orange)"/></svg><span>www.bellwickhomeservice.biz</span></li>
    </ul>
  </div>
</section>

<section class="card card--back">
  <div class="back__brand">
    <div class="brand">
      <div class="brand__mark"></div>
      <div class="brand__name">Bellwick Home Services</div>
    </div>
  </div>
  <svg class="back__stripe" width="560" height="26" viewBox="0 0 560 26">
    <rect x="0" y="8" width="560" height="12" fill="var(--orange)"/>
    <polygon points="420,20 440,4 560,4 560,20" fill="#1d1d1d"/>
  </svg>
</section>

</body>
</html>
```